Council for Stewardship in Civic Ventures Needs a Sponsorship Package Design

We need a print design for a sponsorship package for our 8th Annual BRAVO Summit. Design should implement color and style of Save the Date which is attached. There are multiple layers to this design to include About us (sample attached), letter to sponsors, sponsorship levels, benefits of sponsorship.

There are two parts to the sponsorship. 1 - Forum, 2 - Golf Tournament. A sponsor can decide between one or both of these and receive a $500 discount if choosing a sponsorship from the Forum options and the Golf options.

Sponsor levels and benefits will be added separately through sample from last years package. This format doesn't need to stay the same, but general levels and benefits should be in the package.

Target Market(s)

Design-Build Professionals

Requirements
Must have
• Cover Page
• Letter to Sponsors
• About us, our Mission, why sponsor?
• Contact info
• Sponsor Levels and Benefits for the Forum and Golf Tournament
• Note: Partial proceeds from the golf tournament will provide three $1,000 (?) scholarships: architecture, engineering, and construction
• Agenda, Location Information, place for keynote speakers
Nice to have
• Something that has main elements that can be put on a website.
Should not have
• red

```html
<!DOCTYPE html>
<html lang="en">
<head>
<meta charset="utf-8">
<title>BRAVO Summit – Sponsorship Levels and Benefits</title>
<link href="https://fonts.googleapis.com/css2?family=Source+Sans+3:wght@400;600;700&display=swap" rel="stylesheet">
<style>
  :root{
    --navy:#2f4b9b;
    --navy-deep:#1f2f63;
    --green:#8dc63f;
    --green-light:#c5e08f;
    --ink:#1f1f1f;
    --backdrop:#eef0f5;
    --row-blue:#e9ecf5;
    --row-green:#e8f0da;
    --row-white:#ffffff;
    --grid:#8a93b4;
    --tick:#6b6b6b;
    --footer:#58595b;
  }
  *{box-sizing:border-box;margin:0;padding:0}
  html,body{width:1200px;height:779px;overflow:hidden;background:#fff}
  body{font-family:"Source Sans 3",Arial,sans-serif;color:var(--ink)}
  .spread{position:relative;width:1200px;height:779px;overflow:hidden;background:#fff}
  .page{position:absolute;top:0;height:768px;overflow:hidden}
  .page--levels{left:0;width:600px}
  .page--benefits{left:600px;width:600px}
  .page__art{position:absolute;inset:0;width:100%;height:100%}
  .brand{position:absolute;display:flex;align-items:center;gap:6px}
  .brand__dot{width:22px;height:22px;border-radius:50%;background:var(--navy)}
  .brand__name{font-size:22px;font-weight:700;color:var(--navy);letter-spacing:.5px}
  .page--levels .brand{left:26px;top:86px}
  .page--benefits .brand{left:36px;top:86px}
  .section-title{position:absolute;height:37px;padding:0 12px;display:flex;align-items:center;
    font-size:21px;font-weight:400;line-height:1;white-space:nowrap;color:var(--navy-deep);
    background:linear-gradient(180deg,var(--green-light),var(--green));
    box-shadow:2px 3px 4px rgba(0,0,0,.25)}
  .levels-list{position:absolute;left:28px;list-style:none}
  .levels-list li{position:relative;padding-left:24px;font-size:15px;line-height:19px}
  .levels-list li::before{content:"";position:absolute;left:0;top:4px;width:13px;height:8px;
    border-radius:7px 7px 0 0;background:var(--navy)}
  .levels-list strong{font-weight:700}
  .forum-list{top:242px}
  .forum-list li:nth-child(1){margin-bottom:8px}
  .forum-list li:nth-child(2){margin-bottom:16px}
  .forum-list li:nth-child(3){margin-bottom:16px}
  .forum-list li:nth-child(4){margin-bottom:16px}
  .golf-list{top:549px}
  .golf-list li{margin-bottom:7px}
  .benefits{position:absolute;left:25px;top:224px;width:544px;border-collapse:collapse;table-layout:fixed;
    font-size:7.6px;font-weight:700;line-height:9px}
  .benefits th,.benefits td{border:1px solid var(--grid);padding:0 4px}
  .benefits thead th{background:var(--navy);color:#fff;font-weight:600;font-size:9px;line-height:10.5px;
    text-align:left;vertical-align:top;padding:10px 3px 0;height:67px}
  .benefits thead th small{display:block;font-size:6px;line-height:7px}
  .benefits thead th .limit{display:block;margin-top:9px}
  .benefits thead th.benefits__corner{font-size:8.5px;padding:12px 8px 0}
  .benefits tbody th{text-align:left;font-weight:700;padding-left:8px}
  .benefits tbody td{text-align:center;font-size:10px}
  .benefits tbody tr:nth-child(odd){background:var(--row-blue)}
  .benefits tbody tr:nth-child(even){background:var(--row-green)}
  .benefits tbody tr:nth-child(n+9):nth-child(odd){background:var(--row-white)}
  .benefits tbody td.empty{background:var(--row-white)}
  .tick{display:inline-block;width:4px;height:8px;border:solid var(--tick);border-width:0 2px 2px 0;transform:rotate(40deg)}
  .footer-bar{position:absolute;left:0;bottom:0;width:1200px;height:11px;background:var(--footer)}
</style>
</head>
<body>
<main class="spread">

  <section class="page page--levels">
    <svg class="page__art" viewBox="0 0 600 768" aria-hidden="true">
      <circle cx="300" cy="430" r="400" fill="var(--backdrop)"/>
      <path d="M0 690 Q300 600 600 640 L600 660 Q300 625 0 715 Z" fill="#eef4e2"/>
      <path d="M0 0 L175 0 Q290 60 345 152 Q250 60 70 40 Q30 38 0 44 Z" fill="var(--navy)"/>
      <path d="M150 0 L215 0 Q300 55 345 152 Q280 60 150 0 Z" fill="var(--green)"/>
    </svg>
    <div class="brand"><span class="brand__dot"></span><span class="brand__name">BRAVO</span></div>

    <h2 class="section-title" style="left:25px;top:178px;width:270px">Forum Sponsorship Levels</h2>
    <ul class="levels-list forum-list">
      <li><strong>Partner:</strong> 1 Available<br>($5,000)</li>
      <li><strong>Keynote or Lunch Presentation:</strong><br>3 Available ($3,000)</li>
      <li><strong>Technology:</strong> ($3,000)</li>
      <li><strong>Gold Sponsor:</strong> 4 Available<br>($2,000)</li>
      <li><strong>Silver Sponsor:</strong><br>6 Available ($1,000)</li>
    </ul>

    <h2 class="section-title" style="left:25px;top:497px;width:247px">Golf Sponsorship Levels</h2>
    <ul class="levels-list golf-list">
      <li>Title Sponsor</li>
      <li>Hole Sponsor</li>
      <li>Drink Cart Sponsor</li>
      <li>Lunch Sponsor</li>
      <li>Gift Bag Sponsor</li>
    </ul>
  </section>

  <section class="page page--benefits">
    <svg class="page__art" viewBox="0 0 600 768" aria-hidden="true">
      <circle cx="300" cy="430" r="400" fill="var(--backdrop)"/>
      <path d="M0 690 Q300 600 600 640 L600 660 Q300 625 0 715 Z" fill="#eef4e2"/>
      <path d="M0 0 L180 0 Q295 60 350 152 Q255 60 75 40 Q30 38 0 44 Z" fill="var(--navy)"/>
      <path d="M155 0 L220 0 Q305 55 350 152 Q285 60 155 0 Z" fill="var(--green)"/>
    </svg>
    <div class="brand"><span class="brand__dot"></span><span class="brand__name">BRAVO</span></div>

    <h2 class="section-title" style="left:23px;top:164px;width:232px">Sponsorship Benefits</h2>

    <table class="benefits">
      <colgroup>
        <col style="width:113px"><col style="width:66px"><col style="width:47px"><col style="width:58px">
        <col style="width:45px"><col style="width:47px"><col style="width:51px"><col style="width:59px"><col style="width:58px">
      </colgroup>
      <thead>
        <tr>
          <th class="benefits__corner">SPECIAL EVENT<br>AND OTHER<br>Sponsorship Levels<br>and Benefits</th>
          <th>Technology<br>$ 4,000<span class="limit">Limit 1</span></th>
          <th>Evening Reception<br>$3,500<span class="limit">Limit 1</span></th>
          <th>Lunch Presentation<br>$3,000<span class="limit">Limit 1</span></th>
          <th>Program Printing<br>$2,000<span class="limit">Limit 1</span></th>
          <th>Meet and Greet<br>$1,500<span class="limit">Limit 1</span></th>
          <th>Networking Breakfast<br>$1,500<span class="limit">One per day</span></th>
          <th>Networking Break<br>$750<span class="limit">One per day</span></th>
          <th>Name Badge / Tote<br>$750<small>Limit 1<br>Name Badge 1 Tote</small></th>
        </tr>
      </thead>
      <tbody>
        <tr style="height:34px"><th>Complimentary Conference Registrations</th><td>3</td><td>2</td><td>2</td><td>1</td><td>1</td><td>1</td><td>1</td><td>1</td></tr>
        <tr style="height:36px"><th>Visual Recognition: Sponsor Logo on all print &amp; electronic marketing materials</th><td><span class="tick"></span></td><td><span class="tick"></span></td><td><span class="tick"></span></td><td><span class="tick"></span></td><td><span class="tick"></span></td><td><span class="tick"></span></td><td><span class="tick"></span></td><td><span class="tick"></span></td></tr>
        <tr style="height:32px"><th>Exclusive<br>Representation</th><td><span class="tick"></span></td><td><span class="tick"></span></td><td><span class="tick"></span></td><td><span class="tick"></span></td><td><span class="tick"></span></td><td><span class="tick"></span></td><td><span class="tick"></span></td><td><span class="tick"></span></td></tr>
        <tr style="height:52px"><th>Listing in program as the Event Sponsor next to event description and exclusive event signage</th><td><span class="tick"></span></td><td><span class="tick"></span></td><td><span class="tick"></span></td><td><span class="tick"></span></td><td><span class="tick"></span></td><td><span class="tick"></span></td><td><span class="tick"></span></td><td><span class="tick"></span></td></tr>
        <tr style="height:28px"><th>Firm logo on BRAVO sponsor signage</th><td><span class="tick"></span></td><td><span class="tick"></span></td><td><span class="tick"></span></td><td><span class="tick"></span></td><td><span class="tick"></span></td><td><span class="tick"></span></td><td><span class="tick"></span></td><td><span class="tick"></span></td></tr>
        <tr style="height:28px"><th>Firm introduction/ad in conference program</th><td>Full Page</td><td>½ Page</td><td>¼ Page</td><td>½ Page</td><td>¼ Page</td><td>¼ Page</td><td></td><td></td></tr>
        <tr style="height:28px"><th>Complimentary exhibitor booth</th><td><span class="tick"></span></td><td><span class="tick"></span></td><td><span class="tick"></span></td><td><span class="tick"></span></td><td><span class="tick"></span></td><td><span class="tick"></span></td><td class="empty"></td><td class="empty"></td></tr>
        <tr style="height:27px"><th>Opportunity to include marketing items in tote bags</th><td><span class="tick"></span></td><td><span class="tick"></span></td><td><span class="tick"></span></td><td><span class="tick"></span></td><td><span class="tick"></span></td><td><span class="tick"></span></td><td class="empty"></td><td class="empty"></td></tr>
        <tr style="height:34px"><th>Attendee list with mailing address 2 weeks prior to event</th><td><span class="tick"></span></td><td><span class="tick"></span></td><td><span class="tick"></span></td><td><span class="tick"></span></td><td><span class="tick"></span></td><td><span class="tick"></span></td><td></td><td></td></tr>
        <tr style="height:32px"><th>Attendee list with mailing address 4 weeks prior to event</th><td><span class="tick"></span></td><td><span class="tick"></span></td><td><span class="tick"></span></td><td></td><td></td><td></td><td></td><td></td></tr>
        <tr style="height:33px"><th>Speaking Opportunity (introduce speakers / keynote)</th><td><span class="tick"></span></td><td><span class="tick"></span></td><td><span class="tick"></span></td><td></td><td></td><td></td><td></td><td></td></tr>
        <tr style="height:33px"><th>Logo on one side of conference tote</th><td><span class="tick"></span></td><td></td><td></td><td></td><td></td><td></td><td></td><td></td></tr>
        <tr style="height:35px"><th>Social Media / Press Release Promotion</th><td><span class="tick"></span></td><td></td><td></td><td></td><td></td><td></td><td></td><td></td></tr>
      </tbody>
    </table>
  </section>

  <div class="footer-bar"></div>
</main>
</body>
</html>
```